Zephyr Learning Exhibition Banner

I need an Exhibition banner Designed based of the attached images, along the same lines anyway.

Images must be supplied in .psd format with all layers being able to be edited.

I need a eye catching banner created for a 841 x 2000mm Banner

Dont use all the elements but base your design off the attached flyer and make it look eye catching. little bit of liberty is welcome as long as it looks good

Target Market(s)

School Admin and parents

Requirements
Must have
• submitted in .psd format (photoshop) with all layers able to be edited and not merged

```html
<!DOCTYPE html>
<html lang="en">
<head>
<meta charset="utf-8">
<title>Zephyr Learning – Exhibition Banner</title>
<link rel="stylesheet" href="https://fonts.googleapis.com/css2?family=Oswald:wght@400;500&family=Fira+Sans+Extra+Condensed:wght@600&family=PT+Sans:wght@700&display=swap">
<style>
  :root {
    --brand-blue: #1e5b94;
    --swoosh-grey: #8c8e90;
    --logo-grey: #b4b7ba;
    --page-bg: #d9d9d9;
    --paper: #ffffff;
    --ink-grey: #555555;
  }
  * { margin: 0; padding: 0; box-sizing: border-box; }
  html, body {
    width: 1200px; height: 1200px; overflow: hidden;
    background: var(--page-bg);
  }
  .banner {
    position: absolute; left: 360px; top: 30px;
    width: 480px; height: 1140px;
    background: var(--paper);
    overflow: hidden;
  }
  .banner-shapes { position: absolute; inset: 0; }
  .headline {
    position: absolute; left: 0; right: 0; top: 58px;
    text-align: center;
    font-family: "Oswald", sans-serif; font-weight: 500;
    color: var(--brand-blue); line-height: 1;
  }
  .headline-top { display: block; font-size: 56px; letter-spacing: -0.5px; transform: scaleX(0.9); }
  .headline-main { display: block; font-size: 82px; letter-spacing: -1px; margin-top: 4px; transform: scaleX(0.9); }
  .brand-name {
    position: absolute; left: 34px; top: 722px;
    display: flex; align-items: center; gap: 16px;
    font-family: "Oswald", sans-serif; font-weight: 400;
    font-size: 36px; letter-spacing: 3px; color: var(--logo-grey);
  }
  .brand-mark { width: 30px; height: 30px; background: var(--logo-grey); }
  .pitch {
    position: absolute; right: 29px; top: 888px; text-align: right;
    color: var(--brand-blue);
  }
  .pitch-lead, .pitch-tail {
    font-family: "PT Sans", sans-serif; font-weight: 700; font-size: 19px; line-height: 1.2;
  }
  .pitch-strong {
    font-family: "Fira Sans Extra Condensed", sans-serif; font-weight: 600;
    font-size: 27px; line-height: 1.3; text-transform: uppercase;
  }
  .phone {
    position: absolute; left: 98px; top: 1037px; width: 275px; height: 56px;
    background: var(--brand-blue); border-radius: 10px;
    display: flex; align-items: center; justify-content: center; gap: 14px;
    font-family: "PT Sans", sans-serif; font-weight: 700; font-size: 30px; color: var(--paper);
  }
  .phone svg { width: 24px; height: 24px; }
  .web {
    position: absolute; left: 0; right: 0; top: 1104px; text-align: center;
    font-family: "PT Sans", sans-serif; font-weight: 700; font-size: 13px;
    letter-spacing: 6px; color: var(--ink-grey);
  }
</style>
</head>
<body>
  <main class="banner">
    <svg class="banner-shapes" viewBox="0 0 480 1140" width="480" height="1140">
      <defs>
        <linearGradient id="scene-tone" x1="0" y1="0" x2="0" y2="1">
          <stop offset="0" stop-color="#ffffff"/>
          <stop offset="0.12" stop-color="#e3e5e8"/>
          <stop offset="0.5" stop-color="#bfc3c7"/>
          <stop offset="0.68" stop-color="#8a8c8e"/>
          <stop offset="1" stop-color="#4f5153"/>
        </linearGradient>
      </defs>
      <path class="hero-photo" role="img" aria-label="Photo: a schoolboy with a backpack sitting cross-legged using a laptop, city skyline behind"
            fill="url(#scene-tone)"
            d="M0,205 H480 V635 C400,665 300,650 210,605 C120,560 40,520 0,470 Z"/>
      <path class="swoosh-upper" fill="var(--swoosh-grey)"
            d="M0,374 C10,460 60,520 140,565 C240,620 380,652 480,640 V656 C370,682 230,655 130,605 C60,568 15,515 0,472 Z"/>
      <path class="band-blue" fill="var(--brand-blue)"
            d="M0,523 C40,580 110,632 200,672 C300,712 400,706 480,700 V794 C380,790 250,810 160,860 C90,900 30,950 0,981 Z"/>
      <path class="swoosh-lower" fill="var(--swoosh-grey)"
            d="M480,794 C380,790 250,810 160,860 C110,888 70,918 40,942 C110,890 210,842 300,826 C380,812 440,814 480,822 Z"/>
    </svg>

    <h1 class="headline">
      <span class="headline-top">ORDER YOUR SCHOOL</span>
      <span class="headline-main">LUNCH ONLINE</span>
    </h1>

    <div class="brand-name"><span class="brand-mark"></span>ZEPHYR LEARNING</div>

    <div class="pitch">
      <p class="pitch-lead">Zephyr Learning is an</p>
      <p class="pitch-strong">Extremely safe, secure and<br>convenient online ordering system</p>
      <p class="pitch-tail">for all you school’s&nbsp; requirements.</p>
    </div>

    <div class="phone">
      <svg viewBox="0 0 24 24" aria-hidden="true">
        <circle cx="12" cy="12" r="10.5" fill="none" stroke="#fff" stroke-width="2"/>
        <path fill="#fff" d="M8.6 6.8l1.6-.3 1.1 2.6-1.1.9c.5 1.3 1.5 2.3 2.8 2.9l.9-1.1 2.6 1.1-.3 1.7c-.1.5-.6.9-1.1.8-3.6-.4-6.5-3.3-6.9-6.9 0-.6.3-1.1.8-1.1z"/>
      </svg>
      03 5550 2184
    </div>

    <p class="web">www.zephyrlearning.com.au</p>
  </main>
</body>
</html>
```